PINE HOLLOW BUILDERS leave behind sales FLYER 8.5"x11"

We need a high quality advertising flyer 8.5"x11" for our construction company offering kitchen and bathroom remodels. Can be front and back or just the front of the flyer depending on the design. phone number to come
www.brightmortarworks.example

we are also a home inspection company. We will leave this at the home when we are done with our home inspections for our new home owners

Target Market(s)

Home owners

Industry/Entity Type

Residential Construction

Contact Information for Business Card

We want it to match the flyer please

Requirements
Must have
• My logo, my website , my phone number (to come later),
• FL State Lic. #CRC8047163 & Insured
• We Specialize in Bathroom and Kitchen remodeling ,new Construction & Interior or Exterior home Renovations, garages and more! Serving Central Florida for over 15 years.
• Family owned and operated,
• we perform all levels of building and remodeling.
• i wouldn't mind seeing what you come up with for text on the flyer.
Nice to have
• maybe a nice kitchen and bathroom pictures

```html
<!DOCTYPE html>
<html lang="en">
<head>
<meta charset="utf-8">
<title>Pine Hollow Builders – Flyer</title>
<link rel="stylesheet" href="https://fonts.googleapis.com/css2?family=Open+Sans:wdth,wght@75..100,300..800&display=swap">
<style>
  :root {
    --orange: #f39200;
    --ink: #2a2a2a;
    --text: #333333;
    --muted: #9a9a9a;
    --paper: #ffffff;
    --backdrop: #ececec;
  }
  * { margin: 0; padding: 0; box-sizing: border-box; }
  html, body {
    width: 714px; height: 1200px; overflow: hidden;
    background: var(--backdrop);
    font-family: "Open Sans", Arial, sans-serif;
  }
  .canvas { position: relative; width: 714px; height: 1200px; overflow: hidden; }
  .flyer {
    position: absolute; left: 12px; top: 153px;
    width: 435px; height: 564px;
    background: var(--paper);
    transform: scale(1.586); transform-origin: top left;
    box-shadow: 0 1px 3px rgba(0,0,0,.15);
    overflow: hidden;
    color: var(--text);
  }
  .flyer-shapes { position: absolute; inset: 0; }
  .abs { position: absolute; white-space: nowrap; }

  .brand { left: 270px; top: 28px; width: 165px; text-align: center; }
  .brand-mark { width: 34px; height: 34px; background: var(--orange); margin: 0 auto 8px; }
  .brand-name {
    font-size: 13px; font-weight: 700; color: var(--ink);
    letter-spacing: 1px; line-height: 1.25;
  }
  .brand-name span { display: block; font-size: 9px; letter-spacing: 4px; }

  .headline { left: 31px; top: 280px; font-size: 22px; font-weight: 700; color: var(--ink); font-stretch: 85%; }
  .rule { position: absolute; height: 2px; background: #d0d0d0; }
  .rule::before { content: ""; position: absolute; left: 0; top: 0; height: 2px; width: 80px; background: var(--orange); }
  .intro { left: 31px; top: 320px; font-size: 10.2px; line-height: 19px; color: var(--text); }
  .intro b { font-weight: 700; }
  .serving { left: 29px; top: 358px; font-size: 17.5px; font-weight: 700; color: var(--ink); font-stretch: 78%; }
  .serving em { font-style: normal; color: var(--orange); }
  .section-title { left: 31px; top: 392px; font-size: 21px; font-weight: 700; color: var(--orange); font-stretch: 85%; }

  .services { position: absolute; top: 435px; list-style: none; font-size: 10.5px; color: var(--ink); line-height: 19.5px; }
  .services li { position: relative; padding-left: 16px; }
  .services li::before {
    content: ""; position: absolute; left: 0; top: 5px; width: 9px; height: 9px; background: var(--orange);
    clip-path: polygon(50% 0, 100% 25%, 100% 75%, 50% 100%, 0 75%, 0 25%);
  }
  .services .two-line { line-height: 13px; padding-top: 3px; }
  .services .two-line::before { top: 7px; }

  .call-label { left: 31px; top: 505px; font-size: 15px; color: var(--ink); }
  .call-number { left: 31px; top: 526px; font-size: 13px; font-weight: 700; color: var(--ink); display: flex; align-items: center; gap: 4px; }
  .address { left: 172px; top: 526px; width: 193px; text-align: center; font-size: 9.8px; line-height: 14px; color: var(--ink); border-bottom: 1px solid #bdbdbd; padding-bottom: 1px; }
  .web-strip { left: 0; top: 546px; width: 168px; height: 18px; background: var(--orange); }
  .web-strip a { display: block; padding-left: 12px; font-size: 8px; font-weight: 700; color: #fff; text-decoration: none; line-height: 18px; }
</style>
</head>
<body>
<main class="canvas">
  <article class="flyer">
    <svg class="flyer-shapes" width="435" height="564" viewBox="0 0 435 564">
      <defs>
        <linearGradient id="kitchenTones" x1="0" y1="0" x2="1" y2="1">
          <stop offset="0" stop-color="#eeeae2"/>
          <stop offset=".55" stop-color="#d9d2c5"/>
          <stop offset="1" stop-color="#9c8a72"/>
        </linearGradient>
        <linearGradient id="bathTones" x1="0" y1="0" x2="0" y2="1">
          <stop offset="0" stop-color="#c9cfc2"/>
          <stop offset=".5" stop-color="#e4ddd0"/>
          <stop offset="1" stop-color="#b9a88d"/>
        </linearGradient>
      </defs>
      <polygon class="photo-kitchen" role="img" aria-label="Photo of a bright white remodeled kitchen with marble island and bar stools"
        points="0,0 268,0 268,170 170,270 100,270 0,210" fill="url(#kitchenTones)"/>
      <polyline class="photo-edge" points="0,213 100,273 172,273" fill="none" stroke="var(--orange)" stroke-width="5"/>
      <polygon class="photo-bath-small" role="img" aria-label="Photo of a modern bathroom with freestanding tub and glass shower"
        points="258,176 306,203 306,259 258,286 210,259 210,203" fill="url(#bathTones)" stroke="#fff" stroke-width="3"/>
      <polygon class="band-accent" points="371,287 435,252 435,564 371,564" fill="var(--orange)"/>
      <polygon class="photo-bath-large" role="img" aria-label="Photo of a sunlit master bathroom with corner soaking tub and windows"
        points="370,140 436,178 436,254 370,292 304,254 304,178" fill="url(#bathTones)" stroke="#fff" stroke-width="3"/>
      <g class="service-links" stroke="#cfcfcf" stroke-width="1" fill="none">
        <polyline points="146,444 150,449 146,454"/>
        <line x1="150" y1="449" x2="150" y2="490"/>
        <polyline points="246,444 250,449 246,454"/>
        <line x1="250" y1="449" x2="250" y2="470"/>
      </g>
      <g class="icon-pin" fill="none" stroke="#555" stroke-width="1.2" transform="translate(2,18)">
        <path d="M266 495 C260 487 259 484 259 482 a7 7 0 0 1 14 0 c0 2 -1 5 -7 13 z"/>
        <circle cx="266" cy="482" r="2.3"/>
        <path d="M258 495 h16"/>
      </g>
    </svg>

    <div class="abs brand">
      <div class="brand-mark"></div>
      <p class="brand-name">PINE HOLLOW<span>BUILDERS</span></p>
    </div>

    <h1 class="abs headline">We Specialize in</h1>
    <div class="rule" style="left:31px;top:312px;width:105px"></div>
    <p class="abs intro">Bathroom and Kitchen remodeling ,new Construction &amp; Interior<br>or Exterior home Renovations, garages <b>and more!</b></p>
    <h2 class="abs serving">Serving Central Florida for <em>over 15 years</em></h2>
    <h2 class="abs section-title">What We Do?</h2>
    <div class="rule" style="left:31px;top:424px;width:105px"></div>

    <ul class="services" style="left:34px">
      <li>New Construction</li>
      <li>REMODELS</li>
      <li>BATHROOMS</li>
    </ul>
    <ul class="services" style="left:159px">
      <li>BARNS</li>
      <li>REPAIRS</li>
      <li class="two-line">BANK<br>REMODELS</li>
    </ul>
    <ul class="services" style="left:257px">
      <li>KITCHENS</li>
      <li>RENOVATIONS</li>
    </ul>

    <p class="abs call-label">Call now:</p>
    <p class="abs call-number">
      <svg width="10" height="10" viewBox="0 0 24 24" aria-hidden="true"><path fill="var(--ink)" d="M6.6 10.8a15 15 0 0 0 6.6 6.6l2.2-2.2a1 1 0 0 1 1-.25 11.4 11.4 0 0 0 3.6.57 1 1 0 0 1 1 1V20a1 1 0 0 1-1 1A17 17 0 0 1 3 4a1 1 0 0 1 1-1h3.5a1 1 0 0 1 1 1c0 1.25.2 2.45.57 3.6a1 1 0 0 1-.25 1z"/></svg>
      (123) 456-5700
    </p>
    <p class="abs address">ADDRESS LINE 1<br>FL State Lic. #CRC8047163 &amp; Insured</p>

    <div class="abs web-strip"><a href="#">www.brightmortarworks.example</a></div>
  </article>
</main>
</body>
</html>
```